Etiketten-Design für Honiggläser
Die Zusammenarbeit mit Jorek war sehr unkompliziert. Änderungswünsche wurden prompt umgesetzt und die Beratung war hervorragend! Besten Dank für das tolle Etikett!
Zielgruppe
Wir sind Imker und benötigen Etiketten für Honiggläser.
Aufgabenstellung
Siehe Anlage. Es sollen keine Fotos verwendet werden. Grafiken sind in Ordnung.
Etiketten-Design für Honigglas Etiketten-Design für Honigglas"
Format: Etikett für 250-gr.-Honigglas (TO ∅ 63 mm). Standardmaßgrösse 165 × 40 mm Design: schlicht, hochwertig, modern, edel/royal, unkonventionelles Design (weg von Bienen, Waben, Landschaften usw.), dunkle Farbtöne in Kontrast zu heller Schrift, die beiden Textbausteine 'Los Nr. ' sowi..
Attraktives Etiketten-Design für Honig Attraktives Etiketten-Design für Honig"
Wir verkaufen zur Zeit vor allem Waldhonig, streben aber auch einen Blütenhonig an. Das Etikett soll daher entweder den Wald wiederspiegeln oder aber neutral sein, so dass der Schriftzug Waldhonig oder Blütenhonig jeweils eingesetzt werden kann. Wichtig ist mir der Ortszusatz 'aus dem Glottertal..
Etiketten-Design für Produkte eines Familienbetriebs mit Imkerei und Hühnerhaltung Etiketten-Design für Produkte eines Familienbetriebs mit Imkerei und Hühnerhaltung"
1. Zentrale, auf allen Etiketten wiederkehrende Elemente: - Unser Riegelhaus (stilisiert) (Bild beiliegend) - Das Wort 'Moosrain' (Anmerkung: ohne Anführungszeichen) - die zentralen Elemente sollen die Produkte nicht überragen. 2. Dezente Adresse: - Familie Drabbel, Lindacker, CH-9612 Fallmatt 3...
Etiketten-Design für Kurkuma-Honig Etiketten-Design für Kurkuma-Honig"
Etikett für 500g // Stanze eckig (210x35mm), Druckdatei entsprechend Vorgaben https://klebeprofi-muster.de/faq/ Vorgaben für das Ackerwert Logo im Anhang Vorgaben für EG Öko Logo : https://oeko-siegel-beispiel.eu/downloads/logo_de Pflichtangaben auf dem Etikett: Gewicht, Adresse siehe Beispiel..
Etiketten-Design für Blütenhonig und Waldhonig gesucht Etiketten-Design für Blütenhonig und Waldhonig gesucht"
Zwei verschiedene Etiketten-Desings 1 x Blütenhonig sowie 1 x Waldhonig für unterschiedliche Honigglasgrößen (500 g und 250 g) Die Maße für die Etiketten wären: Für 500-Gramm-Glas 210 mm x 45 mm für's 250-Gramm-Glas 180 mm x 38 mm. Wir sind auch offen für neue Vorschläge bezüglich ..

```html
<!DOCTYPE html>
<html lang="de">
<head>
<meta charset="utf-8">
<title>Bayerischer Bienenhonig – Etikettenserie</title>
<link rel="stylesheet" href="https://fonts.googleapis.com/css2?family=Barlow:wght@400;600&family=Barlow+Condensed:wght@500&family=Sacramento&display=swap">
<style>
  :root {
    --bg-top: #f7efdf;
    --bg-bottom: #efe0c4;
    --label-paper: #efe9dd;
    --panel-white: #ffffff;
    --panel-frame: #9a9a9a;
    --ink: #2b2b2b;
    --ink-soft: #6a6a6a;
    --fruh: #c8694c;
    --fruh-art-a: #f4c9c4;
    --fruh-art-b: #e48f8a;
    --sommer: #f2a900;
    --sommer-art-a: #f8dba0;
    --sommer-art-b: #eeb250;
    --spaet: #8db36b;
    --spaet-art-a: #f5f1e2;
    --spaet-art-b: #d9d27a;
  }
  * { box-sizing: border-box; margin: 0; padding: 0; }
  html, body { width: 1200px; height: 615px; overflow: hidden; }
  body {
    position: relative;
    background: linear-gradient(180deg, var(--bg-top) 0%, var(--bg-bottom) 100%);
    font-family: "Barlow", sans-serif;
    color: var(--ink);
  }

  .label-set { position: absolute; top: 102px; width: 303px; height: 338px; }
  .label-set--fruh   { left: 97px; }
  .label-set--sommer { left: 459px; }
  .label-set--spaet  { left: 823px; }

  /* vertical neck strip */
  .neck-strip {
    position: absolute; left: 125px; top: 0;
    width: 53px; height: 210px;
    background: var(--label-paper);
    text-align: center;
  }
  .neck-strip__art { height: 36px; width: 100%; }
  .neck-strip__info {
    margin-top: 6px; padding: 0 4px;
    font-size: 4.2px; line-height: 1.45; color: var(--ink-soft);
  }
  .neck-strip__info strong { display: block; margin-top: 7px; color: var(--ink); font-weight: 600; }
  .neck-strip__lot {
    display: block; margin: 9px auto 0; width: 46px; height: 12px;
    background: var(--panel-white); border: 0.6px solid var(--panel-frame);
  }
  .neck-strip__weight {
    margin-top: 16px; font-family: "Barlow Condensed", sans-serif;
    font-size: 12.5px; font-weight: 500; color: var(--ink);
  }
  .neck-strip__rule { width: 14px; height: 0.6px; background: var(--ink); margin: 5px auto 0; }
  .neck-strip__address { margin-top: 6px; font-size: 4px; line-height: 1.5; color: var(--ink-soft); }
  .neck-strip__address strong { color: var(--ink); font-weight: 600; }

  /* horizontal wrap band */
  .wrap-band {
    position: absolute; left: 0; top: 210px;
    width: 303px; height: 128px;
    background: var(--label-paper);
  }
  .wrap-band__art { position: absolute; inset: 0; }
  .title-panel {
    position: absolute; left: 78px; top: 21px;
    width: 148px; height: 85px;
    background: var(--panel-white);
    padding: 4px;
  }
  .title-panel__frame {
    width: 100%; height: 100%;
    border: 0.7px solid var(--panel-frame);
    text-align: center;
    padding-top: 5px;
  }
  .title-panel__mark {
    display: block; width: 8px; height: 8px; margin: 0 auto;
    border-radius: 50%; background: var(--ink);
  }
  .title-panel__kicker {
    margin-top: 3px; font-size: 6px; letter-spacing: 3px; color: var(--ink);
  }
  .title-panel__product {
    font-family: "Barlow Condensed", sans-serif; font-weight: 500;
    font-size: 24px; line-height: 1; letter-spacing: 0.2px; margin-top: 1px;
  }
  .title-panel__season {
    font-family: "Sacramento", cursive;
    font-size: 25px; line-height: 0.7; color: var(--ink); margin-top: -2px;
  }
  .title-panel__variety { font-size: 6.5px; color: var(--ink-soft); margin-top: 2px; }

  .label-set--fruh .title-panel__product { color: var(--fruh); }
  .label-set--sommer .title-panel__product { color: var(--sommer); }
  .label-set--spaet .title-panel__product { color: var(--spaet); }

  .label-set--fruh .wrap-band__art,
  .label-set--fruh .neck-strip__art { background: radial-gradient(circle at 20% 40%, var(--fruh-art-b), transparent 45%), radial-gradient(circle at 85% 45%, var(--fruh-art-b), transparent 40%), linear-gradient(135deg, var(--fruh-art-a), var(--label-paper)); }
  .label-set--sommer .wrap-band__art,
  .label-set--sommer .neck-strip__art { background: radial-gradient(circle at 12% 30%, var(--sommer-art-b), transparent 40%), radial-gradient(circle at 90% 75%, var(--sommer-art-b), transparent 40%), linear-gradient(135deg, var(--sommer-art-a), var(--label-paper)); }
  .label-set--spaet .wrap-band__art,
  .label-set--spaet .neck-strip__art { background: radial-gradient(circle at 15% 60%, var(--spaet-art-b), transparent 40%), radial-gradient(circle at 88% 35%, var(--spaet-art-b), transparent 40%), linear-gradient(135deg, var(--spaet-art-a), var(--label-paper)); }
</style>
</head>
<body>

<section class="label-set label-set--fruh">
  <div class="neck-strip">
    <div class="neck-strip__art" role="img" aria-label="Aquarellierte rosa Blüte"></div>
    <p class="neck-strip__info">Bienenhonig kristallisiert bei längerer Lagerung. Durch Erwärmen im Wasserbad bei 40°C kann Honig ohne Schaden wieder verflüssigt werden.
      <strong>Lagerhinweis:</strong>Kühl, dunkel und trocken lagern.
      <strong>Ursprungsland:</strong>Deutschland</p>
    <span class="neck-strip__lot"></span>
    <p class="neck-strip__weight">500g</p>
    <div class="neck-strip__rule"></div>
    <p class="neck-strip__address"><strong>Imkerei Brenntal</strong><br>Wiesengrund 12<br>85999 Hopfenau<br>info@imkerei-brenntal.de</p>
  </div>
  <div class="wrap-band">
    <div class="wrap-band__art" role="img" aria-label="Gezeichnete rosa Frühlingsblüten mit Hummel"></div>
    <div class="title-panel"><div class="title-panel__frame">
      <span class="title-panel__mark"></span>
      <p class="title-panel__kicker">BAYERISCHER</p>
      <p class="title-panel__product">BIENENHONIG</p>
      <p class="title-panel__season">Frühtracht</p>
      <p class="title-panel__variety">Blütenhonig cremig gerührt</p>
    </div></div>
  </div>
</section>

<section class="label-set label-set--sommer">
  <div class="neck-strip">
    <div class="neck-strip__art" role="img" aria-label="Aquarellierte gelbe Sommerblüte"></div>
    <p class="neck-strip__info">Bienenhonig kristallisiert bei längerer Lagerung. Durch Erwärmen im Wasserbad bei 40°C kann Honig ohne Schaden wieder verflüssigt werden.
      <strong>Lagerhinweis:</strong>Kühl, dunkel und trocken lagern.
      <strong>Ursprungsland:</strong>Deutschland</p>
    <span class="neck-strip__lot"></span>
    <p class="neck-strip__weight">500g</p>
    <div class="neck-strip__rule"></div>
    <p class="neck-strip__address"><strong>Imkerei Brenntal</strong><br>Wiesengrund 12<br>85999 Hopfenau<br>info@imkerei-brenntal.de</p>
  </div>
  <div class="wrap-band">
    <div class="wrap-band__art" role="img" aria-label="Gezeichnete gelbe Sommerblüten mit Hummeln"></div>
    <div class="title-panel"><div class="title-panel__frame">
      <span class="title-panel__mark"></span>
      <p class="title-panel__kicker">BAYERISCHER</p>
      <p class="title-panel__product">BIENENHONIG</p>
      <p class="title-panel__season">Sommertracht</p>
      <p class="title-panel__variety">Blütenhonig &amp; Honigtau</p>
    </div></div>
  </div>
</section>

<section class="label-set label-set--spaet">
  <div class="neck-strip">
    <div class="neck-strip__art" role="img" aria-label="Aquarellierte weiße Blüte"></div>
    <p class="neck-strip__info">Bienenhonig kristallisiert bei längerer Lagerung. Durch Erwärmen im Wasserbad bei 40°C kann Honig ohne Schaden wieder verflüssigt werden.
      <strong>Lagerhinweis:</strong>Kühl, dunkel und trocken lagern.
      <strong>Ursprungsland:</strong>Deutschland</p>
    <span class="neck-strip__lot"></span>
    <p class="neck-strip__weight">500g</p>
    <div class="neck-strip__rule"></div>
    <p class="neck-strip__address"><strong>Imkerei Brenntal</strong><br>Wiesengrund 12<br>85999 Hopfenau<br>info@imkerei-brenntal.de</p>
  </div>
  <div class="wrap-band">
    <div class="wrap-band__art" role="img" aria-label="Gezeichnete weiße Spätsommerblüten mit Hummeln und Blättern"></div>
    <div class="title-panel"><div class="title-panel__frame">
      <span class="title-panel__mark"></span>
      <p class="title-panel__kicker">BAYERISCHER</p>
      <p class="title-panel__product">BIENENHONIG</p>
      <p class="title-panel__season">Spättracht</p>
      <p class="title-panel__variety">Waldhonig</p>
    </div></div>
  </div>
</section>

</body>
</html>
```